Reaching the Root: Reasoning in Clinical Choice-Making

I'd like a cover that looks like it would fit on the shelf next to "The Symptom Mirage" by Harold Vintner, "The Fall of Forgetting" by Carl Mortenson, "Meal Mend" by Neil Forsby, "The Energy Renewal Plan" by Owen Prichardson or "The Gland Renewal Plan" by the same or "The Cortex Renewal Plan" by the same ... either text only (with some interesting fonts that make the title stand out, and the subtitle smaller) or a relevant image, though I'm not entirely sure what that would be since this is a book about big-picture medical decision making.
Author name is Dr Miriam Oakhurst, NMD
I'll eventually request an e-book, paperback, and audio cover from the winner...

Target Market(s)

practicing physicians

Industry/Entity Type

medicine

Requirements
Must have
• look similar to other books in the genre

```html
<!DOCTYPE html>
<html lang="en">
<head>
<meta charset="utf-8">
<title>Reaching the Root: Reasoning in Clinical Choice-Making — Cover Wrap</title>
<link rel="stylesheet" href="https://fonts.googleapis.com/css2?family=Bebas+Neue&family=Arimo:wght@400;700&family=Jost:wght@400&display=swap">
<style>
  :root {
    --backdrop: #ecc58c;
    --paper: #fefcf6;
    --teal: #72afb5;
    --grey: #858585;
    --ink: #1c1c1c;
    --block: #040404;
  }
  html, body {
    margin: 0;
    padding: 0;
    width: 1200px;
    height: 893px;
    overflow: hidden;
    background: var(--backdrop);
  }
  .cover-wrap {
    position: absolute;
    left: 43px;
    top: 72px;
    width: 1114px;
    height: 741px;
    background: var(--paper);
  }
  .layer {
    position: absolute;
    inset: 0;
    width: 1114px;
    height: 741px;
  }
  .title-display { font-family: "Bebas Neue", "Oswald", sans-serif; fill: var(--teal); }
  .subtitle { font-family: "Arimo", Arial, sans-serif; fill: var(--grey); }
  .author { font-family: "Arimo", Arial, sans-serif; font-weight: 700; fill: var(--ink); }
  .back-blurb {
    position: absolute;
    left: 43px;
    top: 150px;
    width: 456px;
    margin: 0;
    font-family: "Jost", "Century Gothic", sans-serif;
    font-size: 13.2px;
    line-height: 18.8px;
    color: var(--ink);
    text-align: justify;
  }
  .back-blurb p { margin: 0 0 9.5px; }
  .isbn-block {
    position: absolute;
    left: 290px;
    top: 590px;
    width: 213px;
    height: 98px;
    background: var(--block);
  }
  .cube-art {
    position: absolute;
    left: 862px;
    top: 406px;
    width: 206px;
    height: 206px;
    background: radial-gradient(circle at 50% 55%, #d9dce3 0%, #c9ccd4 35%, #b55a50 60%, rgba(254,252,246,0) 72%);
  }
</style>
</head>
<body>
<main class="cover-wrap">

  <section class="back-cover">
    <div class="back-blurb">
      <p>Lorem ipsum dolor sit amet, consectetur adipiscing elit, sed do eiusmod tempor incididunt ut labore et dolore magna aliqua. Ut enim ad minim veniam, quis nostrud exercitation ullamco laboris nisi ut aliquip ex ea commodo consequat. Duis aute irure dolor in reprehenderit in voluptate velit esse cillum dolore eu fugiat nulla pariatur. Excepteur sint occaecat cupidatat non proident, sunt in culpa qui officia deserunt mollit anim id est laborum.</p>
      <p>Lorem ipsum dolor sit amet, consectetur adipiscing elit, sed do eiusmod tempor incididunt ut labore et dolore magna aliqua. Ut enim ad minim veniam, quis nostrud exercitation ullamco laboris nisi ut aliquip ex ea commodo consequat. Duis aute irure dolor in reprehenderit in voluptate velit esse cillum dolore eu fugiat nulla pariatur. Excepteur sint occaecat cupidatat non proident, sunt in culpa qui officia deserunt mollit anim id est laborum.</p>
      <p>Lorem ipsum dolor sit amet, consectetur adipiscing elit, sed do eiusmod tempor incididunt ut labore et dolore magna aliqua. Ut enim ad minim veniam, quis nostrud exercitation ullamco laboris nisi ut aliquip ex ea commodo consequat. Duis aute irure dolor in reprehenderit in voluptate velit esse cillum dolore eu fugiat nulla pariatur. Excepteur sint occaecat cupidatat non proident, sunt in culpa qui officia deserunt mollit anim id est laborum.</p>
    </div>
    <div class="isbn-block"></div>
  </section>

  <div class="cube-art" role="img" aria-label="3D twisted puzzle cube with red, green, white and blue tiles"></div>

  <svg class="layer" viewBox="0 0 1114 741" xmlns="http://www.w3.org/2000/svg">
    <!-- back cover heading -->
    <g class="back-heading">
      <text class="title-display" x="157" y="79" font-size="50" textLength="241" lengthAdjust="spacingAndGlyphs">REACHING THE ROOT:</text>
      <text class="subtitle" x="158" y="105" font-size="26" textLength="240" lengthAdjust="spacingAndGlyphs">REASONING IN CLINICAL</text>
      <text class="subtitle" x="158" y="128" font-size="26" textLength="236" lengthAdjust="spacingAndGlyphs">CHOICE-MAKING</text>
    </g>

    <!-- spine -->
    <g class="spine" transform="translate(547 39) rotate(90)">
      <text class="title-display" x="0" y="-2" font-size="44" textLength="212" lengthAdjust="spacingAndGlyphs">REACHING THE ROOT:</text>
      <text class="subtitle" x="232" y="-17" font-size="19" textLength="187" lengthAdjust="spacingAndGlyphs">REASONING IN CLINICAL</text>
      <text class="subtitle" x="232" y="-1" font-size="19" textLength="187" lengthAdjust="spacingAndGlyphs">CHOICE-MAKING</text>
      <text class="author" x="438" y="-14" font-size="19" textLength="232" lengthAdjust="spacingAndGlyphs">Dr Miriam Oakhurst, NMD</text>
    </g>

    <!-- front cover -->
    <g class="front-title">
      <text class="title-display" x="622" y="197" font-size="180" textLength="438" lengthAdjust="spacingAndGlyphs">REACHING</text>
      <text class="title-display" x="615" y="343" font-size="180" textLength="445" lengthAdjust="spacingAndGlyphs">THE ROOT:</text>
    </g>
    <g class="front-subtitle">
      <text class="subtitle" x="630" y="453" font-size="53" textLength="210" lengthAdjust="spacingAndGlyphs">REASONING</text>
      <text class="subtitle" x="630" y="492" font-size="53" textLength="212" lengthAdjust="spacingAndGlyphs">IN CLINICAL</text>
      <text class="subtitle" x="630" y="532" font-size="53" textLength="166" lengthAdjust="spacingAndGlyphs">CHOICE</text>
      <text class="subtitle" x="629" y="571" font-size="53" textLength="207" lengthAdjust="spacingAndGlyphs">-MAKING</text>
    </g>
    <text class="author" x="657" y="709" font-size="36" textLength="378" lengthAdjust="spacingAndGlyphs">Dr Miriam Oakhurst, NMD</text>
  </svg>

</main>
</body>
</html>
```